Larkfield civic consultancy needs a business card design

Business card should represent civil engineering infrastructure projects such as roads, bridges, tunnels, rail, rail, pipelines, structures and resource infrastructure

```html
<!DOCTYPE html>
<html lang="en">
<head>
<meta charset="utf-8">
<title>Larkfield Civic Consultancy – Business Card</title>
<link rel="stylesheet" href="https://fonts.googleapis.com/css2?family=Lato:wght@400;700&display=swap">
<style>
  :root{
    --stage:#3a3a3c;
    --navy:#233e7d;
    --white:#ffffff;
    --ink:#1c1c1c;
    --tab:#0a0a0a;
    --silver:#e4e6ea;
  }
  *{margin:0;padding:0;box-sizing:border-box}
  html,body{width:1200px;height:901px;overflow:hidden}
  body{background:var(--stage);font-family:"Lato",Arial,sans-serif;position:relative}
  .card{position:absolute;top:301px;width:520px;height:298px;overflow:hidden;box-shadow:0 10px 24px rgba(0,0,0,.45)}
  .card-front{left:50px;background:var(--white)}
  .card-back{left:630px;background:var(--navy)}

  .front-band{position:absolute;left:0;right:0;bottom:0;height:38px;background:var(--navy)}
  .front-tab{position:absolute;width:12px;height:46px;background:var(--tab)}
  .front-tab--left{left:0;top:176px}
  .front-tab--right{right:0;top:22px}

  .brand{position:absolute;display:flex;align-items:center;gap:10px}
  .brand-square{width:22px;height:22px;border:2px solid currentColor;flex:none}
  .brand-name{font-weight:700;text-transform:uppercase;letter-spacing:.04em;line-height:1.15}
  .card-front .brand{right:30px;top:30px;color:var(--navy)}
  .card-front .brand-name{font-size:14px;width:130px}

  .holder{position:absolute;left:28px;top:150px}
  .holder-name{color:var(--navy);font-size:19px;font-weight:700;text-transform:uppercase;letter-spacing:.02em}
  .holder-role{color:var(--ink);font-size:11px;margin-top:3px}

  .contacts{position:absolute;left:220px;top:178px;list-style:none;color:var(--ink);font-size:11px}
  .contacts li{display:flex;align-items:center;gap:8px;height:18px}
  .contacts svg{width:12px;height:12px;flex:none}

  .card-back .brand{left:50%;top:50%;transform:translate(-50%,-50%);flex-direction:column;gap:14px;color:var(--silver);text-align:center}
  .card-back .brand-square{width:30px;height:30px}
  .card-back .brand-name{font-size:16px;width:220px}
</style>
</head>
<body>
  <section class="card card-front" aria-label="Business card front">
    <div class="front-tab front-tab--left"></div>
    <div class="front-tab front-tab--right"></div>

    <div class="brand">
      <span class="brand-square"></span>
      <span class="brand-name">Larkfield Civic Consultancy</span>
    </div>

    <div class="holder">
      <p class="holder-name">Owen Castell Reyes</p>
      <p class="holder-role">Director</p>
    </div>

    <ul class="contacts">
      <li>
        <svg viewBox="0 0 12 12"><rect x="3" y="0.5" width="6" height="11" rx="1" fill="none" stroke="#233e7d" stroke-width="1.2"/></svg>
        +61 400 527 319
      </li>
      <li>
        <svg viewBox="0 0 12 12"><rect x="0.5" y="2" width="11" height="8" fill="#233e7d"/><path d="M0.5 2 6 6.5 11.5 2" fill="none" stroke="#fff" stroke-width="1"/></svg>
        owen.reyes@mailhub.com.au
      </li>
      <li>
        <svg viewBox="0 0 12 12"><rect x="0.5" y="2" width="11" height="8" fill="#233e7d"/><path d="M0.5 2 6 6.5 11.5 2" fill="none" stroke="#fff" stroke-width="1"/></svg>
        owen.reyes@larkfieldcivic.com.au
      </li>
    </ul>

    <div class="front-band"></div>
  </section>

  <section class="card card-back" aria-label="Business card back">
    <div class="brand">
      <span class="brand-square"></span>
      <span class="brand-name">Larkfield Civic Consultancy</span>
    </div>
  </section>
</body>
</html>
```